Modern Brochure Design for Music School !!

I would like to have a brochure (A4 two fold) created for my partners music school. I would like it to incorporate information from his website, showing what classes are taught (singing lessons, drum lessons, guitar lessons and keyboard lessons). I would like to keep the same font style or as close to what's on the website if possible.

It needs to grab attention and be modern in design to attract age group of 18-35 while briefly detailing what services they provide, including their location and phone number

Info can all be found on the website www.thevocalloftstudio.com.au

Target Market(s)

18-35 y/o

Industry/Entity Type

School

Font styles to use
Serif

Colors
000000

Requirements
Must have
• Key content from website
• List of classes (singing, drums, guitar, keyboard)
• Address / phone number
• Find us on Facebook - The Vocal Loft Studio /Instagram @the_vocal_loft_studio
• Mention - gift vouchers available
• Black and white colours preferably no bright colours (like website)
• Modern and professional please!!
Nice to have
• Same type font as website or close to
• Not too much content

```html
<!DOCTYPE html>
<html lang="en">
<head>
<meta charset="utf-8">
<title>The Vocal Loft Studio – Brochure</title>
<link href="https://fonts.googleapis.com/css2?family=Dosis:wght@300;400;600;700&display=swap" rel="stylesheet">
<style>
  :root {
    --backdrop: #5e5d5e;
    --ink: #000000;
    --paper: #ffffff;
    --panel: rgba(8, 8, 8, 0.88);
    --text-light: #f2f2f2;
    --text-dark: #1a1a1a;
  }
  * { margin: 0; padding: 0; box-sizing: border-box; }
  html, body { width: 1200px; height: 1200px; overflow: hidden; }
  body {
    background: var(--backdrop);
    font-family: "Dosis", "Arial Narrow", sans-serif;
    position: relative;
  }
  .spread {
    position: absolute;
    left: 82px;
    width: 1036px;
    height: 519px;
    overflow: hidden;
  }
  .spread--cover { top: 67px; background: var(--paper); }
  .spread--inside { top: 614px; background: var(--ink); }
  .spread svg.art { position: absolute; inset: 0; }

  /* cover */
  .contacts {
    position: absolute; left: 0; top: 175px; width: 267px; height: 168px;
    background: var(--panel); color: var(--text-light);
    padding: 38px 0 0 37px;
  }
  .contacts h3 { font-weight: 700; font-size: 12.5px; letter-spacing: .2px; margin-bottom: 4px; }
  .contacts li {
    list-style: none; display: flex; align-items: center; gap: 7px;
    font-size: 9.5px; height: 18px; color: #d8d8d8;
  }
  .contacts .ico {
    width: 11px; height: 11px; border-radius: 50%; background: #e8e8e8;
    display: flex; align-items: center; justify-content: center; flex: none;
  }
  .studio-name {
    position: absolute; left: 675px; top: 232px; width: 205px;
    color: var(--text-light); text-align: center;
    font-weight: 600; font-size: 24px; line-height: 1.1; letter-spacing: .5px;
  }

  /* inside */
  .txt { position: absolute; text-align: center; font-weight: 400; line-height: 1; }
  .mission { color: #e6e6e6; left: 20px; width: 480px; }
  .lead { top: 52px; font-size: 14px; }
  .hero { top: 74px; font-size: 40px; font-weight: 300; color: #f4f4f4; letter-spacing: .5px; }
  .sub { font-size: 14.5px; }
  .belief { left: 150px; width: 290px; color: var(--text-dark); font-size: 24px; font-weight: 300; line-height: 1.36; top: 374px; }
  .lessons-title { left: 553px; top: 40px; text-align: left; color: #efefef; font-size: 32px; font-weight: 300; }
  .lessons-kicker { left: 555px; top: 76px; text-align: left; color: #d8d8d8; font-size: 9.5px; }
  .col {
    position: absolute; width: 86px; text-align: center;
    font-size: 9.3px; line-height: 1.3; color: var(--text-dark);
  }
  .promo { left: 580px; width: 150px; top: 438px; color: #e8e8e8; font-size: 9.3px; line-height: 1.25; }
  .promo b { font-weight: 700; }
  .slogan { left: 774px; top: 360px; text-align: left; color: #f4f4f4; font-size: 31px; font-weight: 300; line-height: .98; }
  .slogan .small { font-size: 9.5px; display: block; margin: 6px 0 0 120px; letter-spacing: 1px; }
  .slogan .row { display: flex; align-items: baseline; margin-left: 17px; margin-top: 2px; }
  .slogan .row .small { margin: 0 2px 0 0; display: inline; }
  .slogan .big { font-size: 34px; }
</style>
</head>
<body>

<section class="spread spread--cover">
  <svg class="art" width="1036" height="519" viewBox="0 0 1036 519">
    <defs>
      <radialGradient id="micGlow" cx="0.55" cy="0.45" r="0.6">
        <stop offset="0" stop-color="#8c8c8c"/>
        <stop offset="0.5" stop-color="#444"/>
        <stop offset="1" stop-color="#111"/>
      </radialGradient>
      <linearGradient id="bandShade" x1="0" x2="1">
        <stop offset="0" stop-color="#fff"/>
        <stop offset="0.48" stop-color="#d8d8d8"/>
        <stop offset="0.52" stop-color="#fff"/>
        <stop offset="1" stop-color="#c9c9c9"/>
      </linearGradient>
    </defs>
    <rect width="1036" height="22" fill="url(#bandShade)"/>
    <rect y="497" width="1036" height="22" fill="url(#bandShade)"/>
    <rect y="22" width="1036" height="475" fill="url(#micGlow)" role="img" aria-label="Black and white photograph of a studio condenser microphone in a shock mount"/>
    <line x1="518" y1="0" x2="518" y2="519" stroke="#000" stroke-opacity=".15"/>
  </svg>

  <div class="contacts">
    <h3>BUSINESS CONTACTS:</h3>
    <ul>
      <li><span class="ico"><svg width="7" height="7" viewBox="0 0 10 10"><path d="M5 0a3.5 3.5 0 0 0-3.5 3.5C1.5 6 5 10 5 10s3.5-4 3.5-6.5A3.5 3.5 0 0 0 5 0z" fill="#000"/><circle cx="5" cy="3.5" r="1.3" fill="#e8e8e8"/></svg></span>118 Carrington Road Box Hill Victoria</li>
      <li><span class="ico"><svg width="7" height="7" viewBox="0 0 10 10"><path d="M2 0l2 2.5-1 1.5c.6 1.3 1.6 2.3 3 3l1.5-1L10 8l-1.5 2C4 10 0 6 0 1.5z" fill="#000"/></svg></span>1300 555 019</li>
      <li><span class="ico"><svg width="7" height="7" viewBox="0 0 10 10"><path d="M0 1l10 4-10 4 2-4z" fill="#000"/></svg></span>info@thevocalloftstudio.com.au</li>
      <li><span class="ico"><svg width="7" height="7" viewBox="0 0 10 10"><rect x="1" y="1" width="8" height="8" rx="1.5" fill="#000"/></svg></span>The Vocal Loft Studio</li>
      <li><span class="ico"><svg width="7" height="7" viewBox="0 0 10 10"><circle cx="5" cy="5" r="4" fill="#000"/></svg></span>@the_vocal_loft_studio</li>
    </ul>
  </div>

  <div class="studio-name">THE VOCAL LOFT<br>STUDIO</div>
</section>

<section class="spread spread--inside">
  <svg class="art" width="1036" height="519" viewBox="0 0 1036 519">
    <defs>
      <radialGradient id="crowd" cx="0.45" cy="0.35" r="0.7">
        <stop offset="0" stop-color="#9a9a9a"/>
        <stop offset="0.55" stop-color="#3c3c3c"/>
        <stop offset="1" stop-color="#0c0c0c"/>
      </radialGradient>
      <radialGradient id="stage" cx="0.3" cy="0.2" r="0.8">
        <stop offset="0" stop-color="#7a7a7a"/>
        <stop offset="0.5" stop-color="#2a2a2a"/>
        <stop offset="1" stop-color="#050505"/>
      </radialGradient>
      <linearGradient id="strip" x1="0" x2="1">
        <stop offset="0" stop-color="#c4c4c4"/>
        <stop offset="1" stop-color="#f6f6f6"/>
      </linearGradient>
      <linearGradient id="bandLeft" x1="0" x2="1" y1="1" y2="0">
        <stop offset="0" stop-color="#ffffff"/>
        <stop offset="1" stop-color="#dcdcdc"/>
      </linearGradient>
      <clipPath id="bandClip">
        <polygon points="0,430 926,0 1036,0 1036,166 358,519 0,519"/>
      </clipPath>
    </defs>
    <rect width="518" height="519" fill="url(#crowd)" role="img" aria-label="Black and white photograph of a concert crowd silhouetted against stage lights"/>
    <rect x="518" width="518" height="519" fill="url(#stage)" role="img" aria-label="Black and white photograph of a performer on stage and a drum kit"/>
    <g clip-path="url(#bandClip)">
      <rect width="1036" height="519" fill="url(#bandLeft)"/>
      <rect x="518" width="104" height="519" fill="url(#strip)"/>
      <rect x="622" width="104" height="519" fill="url(#strip)"/>
      <rect x="726" width="104" height="519" fill="url(#strip)"/>
      <rect x="830" width="104" height="519" fill="url(#strip)"/>
      <rect x="934" width="102" height="519" fill="url(#strip)"/>
    </g>
  </svg>

  <div class="txt mission lead">WE STRIVE TO MAKE THE WORLD A NICER PLACE TO BE IN,</div>
  <div class="txt mission hero">ONE VOICE AT A TIME</div>
  <div class="txt mission sub" style="top:120px">FUN AND AFFORDABLE ONE-ON-ONE VOCAL TUITION</div>
  <div class="txt mission sub" style="top:139px">AND NOW GUITAR, DRUMS AND KEYBOARD TUITION</div>
  <div class="txt mission sub" style="top:161px">ALL AGES – ALL LEVELS OF EXPERIENCE – ALL MODERN VOCAL STYLES</div>
  <div class="txt mission sub" style="top:183px">BRAND NEW LOCATION 118 CARRINGTON RD</div>
  <div class="txt mission sub" style="top:202px">BOX HILL, VICTORIA</div>

  <div class="txt belief">WE BELIEVE THAT<br>ANYONE CAN LEARN<br>HOW TO SING</div>

  <div class="txt lessons-title">LESSONS</div>
  <div class="txt lessons-kicker">START SOMETHING LIKE THIS..</div>

  <p class="col" style="left:527px;top:208px">Lessons with The Vocal Loft Studio generally last for 30 minutes, involve one-on-one tuition and are available Monday through Saturday, between the hours of 12pm and 9pm. Saturdays 10am through to 3pm</p>
  <p class="col" style="left:631px;top:152px">If you require an alternative arrangement, such as group lessons at your home or coaching in the studio while you record that all important demo or EP, we will gladly accommodate such arrangements wherever possible.</p>
  <p class="col" style="left:735px;top:101px">Lessons with Daniel, our Principal Instructor, Monday to Thursday. Lessons with Mia, Tuesdays and Fridays. Owen is the newest member to The Vocal Loft Studio team, teaches Guitar on Monday's. Vocals Monday, Wednesdays and Saturdays.</p>
  <p class="col" style="left:839px;top:96px">Discount rates apply where 10 lessons are paid for in advance, or where a student refers a family member or friend to us.</p>
  <p class="col" style="left:942px;top:13px">We ask that you bring a USB storage device to each lesson, to which we can save your assigned vocal exercises for practicing at home. If you do not have access to a computer at home, we can put your vocal exercises on a CD instead.</p>

  <div class="txt promo">LESSONS ARE AVAILABLE NOW!<br><b>KEYBOARD LESSONS<br>GUITAR LESSONS<br>TEACHING IS OUR PASSION</b></div>

  <div class="txt slogan">THE VOCAL LOFT<br>STUDIO
    <span class="small">HAS GONE</span>
    <span class="row"><span class="small">INSTRU</span><span class="big">MENTAL</span></span>
  </div>
</section>

</body>
</html>
```